Dr. Marissa Tevlin Medical/Chiropractic Business Card

Dr. Tevlin is a chiropractor and will require a business card that she uses every single day to book appointments on the back side of the card. Currently the office name goes by Dr. Marissa Tevlin. The chiropractic profession is based on the diagnosis and manipulative treatment of misalignments of the joints, especially those of the spinal column, which are held to cause other disorders by affecting the nerves, muscles, and organs. Dr. Marissa Tevlin is looking for a contemporary and minimalistic design.

Industry/Entity Type

Medical

Contact Information for Business Card

Name: Dr. Marissa Tevlin; Address: 748 Harcastle Rd South, London, ON N5R 2K7; Phone Number: 519.274.6193; Fax: 519.281.5046; email: marissa.tevlin@quorvamail.com

Requirements
Must have
• ability to write multiple appointments date/time on the back of card

```html
<!DOCTYPE html>
<html lang="en">
<head>
<meta charset="utf-8">
<title>Dr. Marissa Tevlin – Business Card</title>
<link rel="stylesheet" href="https://fonts.googleapis.com/css2?family=Questrial&display=swap">
<style>
  :root{
    --bg:#e7e5e1;
    --card:#ffffff;
    --blue:#3350b8;
    --cyan:#3fc1e4;
    --text:#4a4a4a;
    --rule:#c9c9c9;
    --muted:#9a9a9a;
  }
  *{box-sizing:border-box;margin:0;padding:0}
  html,body{width:1200px;height:973px;overflow:hidden;background:var(--bg);font-family:"Questrial",sans-serif}
  .canvas{position:relative;width:1200px;height:973px}

  .card{position:absolute;background:var(--card);border-radius:20px;overflow:hidden;box-shadow:0 6px 18px rgba(0,0,0,.12)}

  /* Front */
  .card-front{left:60px;top:303px;width:640px;height:366px}
  .front-swoosh{position:absolute;inset:0}
  .name-block{position:absolute;left:176px;top:96px}
  .brand-mark{width:80px;height:80px;background:var(--blue);margin-bottom:16px}
  .doctor-name{font-size:25px;font-weight:400;color:var(--blue);white-space:nowrap;line-height:1.2}
  .doctor-title{font-size:21px;color:var(--cyan);margin-top:4px;line-height:1.2}
  .divider{position:absolute;left:390px;top:70px;width:1px;height:220px;background:var(--cyan)}
  .contacts{position:absolute;left:406px;top:84px;list-style:none;color:var(--text);font-size:14px}
  .contacts li{display:flex;align-items:center;gap:8px;height:26px;white-space:nowrap}
  .contacts svg{width:14px;height:14px;flex:none;fill:var(--blue)}
  .address{position:absolute;left:406px;top:190px;color:var(--text);font-size:14px;line-height:1.7;font-style:normal;white-space:nowrap}

  /* Back */
  .card-back{left:770px;top:176px;width:370px;height:620px}
  .back-brand{position:absolute;left:0;right:0;top:48px;display:flex;flex-direction:column;align-items:center;gap:10px}
  .back-brand .brand-square{width:70px;height:70px;background:var(--blue)}
  .back-brand .brand-name{font-size:14px;color:var(--blue)}
  .appointments-title{position:absolute;left:0;right:0;top:170px;text-align:center;font-size:30px;font-weight:400;color:var(--text)}
  .slots{position:absolute;left:34px;right:34px;top:232px;display:grid;grid-template-columns:1fr 104px;column-gap:18px}
  .slot-head{font-size:18px;color:var(--text);border-bottom:2px solid var(--cyan);padding-bottom:3px}
  .slot-line{height:30px;border-bottom:1px solid var(--rule)}
  .closing{position:absolute;left:34px;right:34px;bottom:34px}
  .closing-rule{height:2px;background:var(--cyan);margin-bottom:12px}
  .closing-note{text-align:center;font-size:12.5px;line-height:1.5;color:var(--muted)}
</style>
</head>
<body>
<main class="canvas">

  <section class="card card-front" aria-label="Business card front">
    <svg class="front-swoosh" viewBox="0 0 640 366" preserveAspectRatio="none" aria-hidden="true">
      <path d="M0,0 H92 C32,120 62,300 370,366 H0 Z" fill="#3fc1e4"/>
      <path d="M0,0 H76 C16,122 46,304 344,366 H0 Z" fill="#ffffff"/>
      <path d="M0,0 H70 C10,124 40,306 330,366 H0 Z" fill="#3350b8"/>
    </svg>
    <div class="name-block">
      <div class="brand-mark" aria-hidden="true"></div>
      <h1 class="doctor-name">Dr. Marissa Tevlin</h1>
      <p class="doctor-title">Chiropractor</p>
    </div>
    <div class="divider"></div>
    <ul class="contacts">
      <li><svg viewBox="0 0 24 24"><path d="M6.6 10.8a15 15 0 0 0 6.6 6.6l2.2-2.2a1 1 0 0 1 1-.25 11.4 11.4 0 0 0 3.6.57 1 1 0 0 1 1 1V20a1 1 0 0 1-1 1A17 17 0 0 1 3 4a1 1 0 0 1 1-1h3.5a1 1 0 0 1 1 1c0 1.25.2 2.45.57 3.6a1 1 0 0 1-.25 1z"/></svg>519-274-6193</li>
      <li><svg viewBox="0 0 24 24"><path d="M6 2h12v6H6zM4 9h16a2 2 0 0 1 2 2v7h-4v4H6v-4H2v-7a2 2 0 0 1 2-2zm4 8v3h8v-3z"/></svg>519-281-5046</li>
      <li><svg viewBox="0 0 24 24"><path d="M2 5h20v14H2zm2 2v.5l8 5 8-5V7zm0 2.8V17h16V9.8l-8 5z"/></svg>marissa.tevlin@quorvamail.com</li>
    </ul>
    <address class="address">748 Harcastle Rd South,<br>London, ON N5R 2K7</address>
  </section>

  <section class="card card-back" aria-label="Business card back">
    <div class="back-brand">
      <div class="brand-square" aria-hidden="true"></div>
      <span class="brand-name">Dr. Marissa Tevlin</span>
    </div>
    <h2 class="appointments-title">Appointments</h2>
    <div class="slots">
      <div class="slot-head">Date</div><div class="slot-head">Time</div>
      <div class="slot-line"></div><div class="slot-line"></div>
      <div class="slot-line"></div><div class="slot-line"></div>
      <div class="slot-line"></div><div class="slot-line"></div>
      <div class="slot-line"></div><div class="slot-line"></div>
      <div class="slot-line"></div><div class="slot-line"></div>
      <div class="slot-line"></div><div class="slot-line"></div>
      <div class="slot-line"></div><div class="slot-line"></div>
      <div class="slot-line"></div><div class="slot-line"></div>
      <div class="slot-line"></div><div class="slot-line"></div>
    </div>
    <div class="closing">
      <div class="closing-rule"></div>
      <p class="closing-note">If you are unable to make your appointment,<br>please call us to reschedule</p>
    </div>
  </section>

</main>
</body>
</html>
```